Bluefern Realty Letterhead

Bluefern Realty Guan
417 Corrin Tide Avenue, Ste B305
Tumon, GU. 96913

Industry/Entity Type

Real Estate

Font styles to use
Serif

Colors

Designer to choose colors to be used in the design.

```html
<!DOCTYPE html>
<html lang="en">
<head>
<meta charset="utf-8">
<title>Bluefern Realty Letterhead</title>
<link href="https://fonts.googleapis.com/css2?family=Open+Sans:wght@400&family=Roboto:wght@400&display=swap" rel="stylesheet">
<style>
  :root {
    --backdrop: #dcdcdc;
    --paper: #f7f7f7;
    --ocean-blue: #138fcc;
    --sun-orange: #f4aa3a;
    --sky-blue: #6ac5e6;
    --brand-blue: #5bbce4;
    --body-text: #4a4a4a;
    --footer-text: #555555;
    --signature-tone: #d9d9d9;
  }
  * { margin: 0; padding: 0; box-sizing: border-box; }
  html, body {
    width: 1153px;
    height: 1200px;
    overflow: hidden;
    background: var(--backdrop);
  }
  .letterhead {
    position: absolute;
    left: 160px;
    top: 20px;
    width: 832px;
    height: 1160px;
    background: var(--paper);
    overflow: hidden;
  }
  .header-wave {
    position: absolute;
    left: 0;
    top: 0;
    width: 832px;
    height: 170px;
  }
  .brand-name {
    position: absolute;
    left: 79px;
    top: 108px;
    font-family: "Open Sans", sans-serif;
    font-weight: 400;
    font-size: 34px;
    letter-spacing: 1px;
    color: var(--brand-blue);
    white-space: nowrap;
  }
  .letter-body {
    position: absolute;
    left: 79px;
    top: 352px;
    width: 682px;
    font-family: "Open Sans", sans-serif;
    font-size: 14.4px;
    line-height: 22.3px;
    color: var(--body-text);
  }
  .salutation { margin-bottom: 22px; }
  .letter-body p.paragraph {
    text-align: justify;
    text-align-last: left;
    margin-bottom: 22.3px;
  }
  .signature-area {
    position: absolute;
    left: 81px;
    top: 819px;
    width: 96px;
    height: 93px;
    background: var(--signature-tone);
    border-radius: 4px;
  }
  .company-footer {
    position: absolute;
    left: 0;
    top: 1074px;
    width: 832px;
    text-align: center;
    font-family: "Roboto", sans-serif;
    font-size: 16.5px;
    line-height: 22px;
    color: var(--footer-text);
  }
  .footer-band {
    position: absolute;
    left: 0;
    bottom: 0;
    width: 832px;
    height: 13px;
    background: var(--sky-blue);
  }
</style>
</head>
<body>
  <main class="letterhead">
    <svg class="header-wave" viewBox="0 0 1008 206" preserveAspectRatio="none" aria-hidden="true">
      <path d="M0 0 H1008 V163 Q430 -5 0 85 Z" fill="var(--ocean-blue)"/>
      <path d="M88 76 Q440 18 1008 170 V203 Q470 38 88 76 Z" fill="var(--sun-orange)"/>
    </svg>

    <div class="brand-name">Bluefern Realty</div>

    <section class="letter-body">
      <p class="salutation">Dear customer,</p>
      <p class="paragraph">Lorem ipsum dolor sit amet, consectetur adipisicing elit, sed do eiusmod tempor incididunt ut labore et dolore magna aliqua. Ut enim ad minim veniam, quis nostrud exercitation ullamco laboris nisi ut aliquip ex ea commodo consequat. Duis aute irure dolor in reprehenderit in voluptate velit esse cillum dolore eu fugiat nulla pariatur. Excepteur sint occaecat cupidatat non proident, sunt in culpa qui officia deserunt mollit anim id est laborum.</p>
      <p class="paragraph">Lorem ipsum dolor sit amet, consectetur adipisicing elit, sed do eiusmod tempor incididunt ut labore et dolore magna aliqua. Ut enim ad minim veniam, quis nostrud exercitation ullamco laboris nisi ut aliquip ex ea commodo consequat. Duis aute irure dolor in reprehenderit in voluptate velit esse cillum dolore eu fugiat nulla pariatur. Excepteur sint occaecat cupidatat non proident, sunt in culpa qui officia deserunt mollit anim id est laborum.</p>
      <p class="paragraph">Lorem ipsum dolor sit amet, consectetur adipisicing elit, sed do eiusmod tempor incididunt ut labore et dolore magna aliqua. Ut enim ad minim veniam, quis nostrud exercitation ullamco laboris nisi ut aliquip ex ea commodo consequat. Duis aute irure dolor in reprehenderit in voluptate velit esse cillum dolore eu fugiat nulla pariatur. Excepteur sint occaecat cupidatat non proident, sunt in culpa qui officia deserunt mollit anim id est laborum.</p>
    </section>

    <div class="signature-area" role="img" aria-label="Handwritten signature of the sender"></div>

    <footer class="company-footer">
      <div class="footer-name">Bluefern Realty Guan</div>
      <div class="footer-address">417 Corrin Tide Avenue, Ste B305 Tumon, GU. 96913</div>
    </footer>

    <div class="footer-band"></div>
  </main>
</body>
</html>
```